Innovative biopolymers technology company needs a professional and engaging website

KLEV Matrexa Technologies AG is a biopolymer technology licensing company that enables plastic compounders to access new markets and innovate, plastic converters to manufacture bio-based, biodegradable, and bio-neutral plastic, and brand owners to satisfy the end-users’ demand for ‘greener’ plastics.

Our purpose is to help mankind ‘savour the ease of everyday goods with a clear mind’. That’s why we’ve developed and patented our KLEVOR® Technology, which enables producing plastics that are ‘quiet on the earth’. Our products are based on renewable materials, up to 99%, and can be – if required – 100% biodegradable at the same time.

Technically our bio plastics could replace 90% of today’s polyethylene applications. Therefore, our vision is ‘to make KLEVOR® the world’s standard for the production and innovation in the area of biopolymers’.

We'd like to see website designs that portray us a serious technology company, whose products benefit the environment and brings alive our brand promise of 'quiet on the earth'.

Target Market(s)

Our primary target audience are plastics compounders that either want to produce resin/pellets, which allow their clients to produce either bio-based or biodegradable plastic.

Industry/Entity Type

Biodegradable

Requirements
Must have
• The website should be designed that it creates the desired user experience, represents the pre-defined structure, and meets our brand guidelines (see attached document KLEV_WebsiteDesignBrief_FinalVersion.pdf). Moreover, it needs to include the prepared content (see attached document KLEV_WebsiteContent_FinalVersion.doc).
Nice to have
• Ideally the selected PressLeaf template should have an ordering functionality build-in already so that at a later stage we could order a product ordering process.
Should not have
• The design shouldn't look like purely an environmental company.

```html
<!DOCTYPE html>
<html lang="en">
<head>
<meta charset="utf-8">
<title>KLEV Matrexa Technologies AG</title>
<link href="https://fonts.googleapis.com/css2?family=Archivo+Black&family=Cabin:wght@400;500&family=Open+Sans:wght@400;600&family=Arimo:wght@400;700&display=swap" rel="stylesheet">
<style>
:root{
  --teal:#2aa3c2;
  --teal-btn:#3ab7d3;
  --ink:#333;
  --muted:#555;
  --line:#dcdcdc;
  --orange:#ef5a1c;
  --footer:#363636;
  --footer-text:#e6e6e6;
}
*{margin:0;padding:0;box-sizing:border-box}
html,body{width:927px;height:1200px;overflow:hidden;background:#fff}
body{position:relative;font-family:"Open Sans",sans-serif;color:var(--ink)}
.abs{position:absolute}

.topbar{top:0;left:0;width:927px;height:27px;border-bottom:1px solid #e2e2e2}
.topbar .item{top:5px;font-size:11px;color:#444;display:flex;align-items:center;gap:7px}
.topbar .phone{font-size:13px}

.logo{left:82px;top:34px}
.logo .name{font-family:"Cabin",sans-serif;font-weight:500;font-size:30px;letter-spacing:1px;color:#111;line-height:1;display:flex;align-items:center;gap:6px}
.logo .name i{display:inline-block;width:10px;height:10px;border-radius:50%;background:var(--teal)}
.logo .tag{font-family:"Cabin",sans-serif;font-size:10px;color:var(--teal);margin-top:3px}

.nav{top:27px;left:0;width:927px}
.nav a{position:absolute;top:24px;font-size:10px;color:#222;text-decoration:none;letter-spacing:.3px}
.nav a.active{color:var(--teal)}
.nav .marker{position:absolute;left:429px;top:0;width:44px;height:2px;background:#3aa0b8}

.hero{top:84px;left:0;width:927px;height:322px;overflow:hidden;
  background:linear-gradient(90deg,#efefed 0%,#e6e4df 35%,#dcd7cf 60%,#e9e8e6 100%)}
.hero .product{position:absolute;left:450px;top:20px;width:380px;height:270px;border-radius:20px;
  background:radial-gradient(ellipse at 60% 80%,#f0a487 0%,#f59a6a 25%,rgba(245,200,120,.7) 50%,rgba(230,230,230,0) 75%)}
.hero h1{position:absolute;left:77px;top:66px;font-family:"Archivo Black",sans-serif;font-size:34px;color:#2b2b2b;letter-spacing:.3px}
.hero .rule{position:absolute;left:78px;width:352px;height:1px;background:#b9b6b1}
.hero .sub{position:absolute;left:79px;top:128px;font-family:"Cabin",sans-serif;font-size:20px;color:#333}
.hero .btn{position:absolute;left:78px;top:189px;width:170px;height:44px;background:var(--teal-btn);border-radius:3px;
  color:#fff;font-family:"Cabin",sans-serif;font-size:16px;display:flex;align-items:center;justify-content:center}
.hero .arrow{position:absolute;top:126px;width:34px;height:39px;background:#8d8b88;border-radius:3px;display:flex;align-items:center;justify-content:center}

.audience h2{font-family:"Cabin",sans-serif;font-weight:400;font-size:18px;color:var(--teal);display:flex;align-items:center;gap:8px}
.audience h2 i{display:inline-block;width:20px;height:20px;border-radius:50%}
.audience p{font-size:10px;line-height:15.5px;letter-spacing:.5px;color:#333;margin-top:10px;width:220px;padding-left:4px}

.divider{left:79px;top:584px;width:769px;height:1px;background:#e4e4e4}

.work .thumb{width:222px;height:124px;border:2px solid #eee}
.work h3{font-family:"Cabin",sans-serif;font-weight:400;font-size:17px;color:#2f8fa8;margin-top:6px}
.work .meta{font-size:9px;letter-spacing:.8px;color:#444;margin-top:3px}

.contact{left:610px;top:625px;width:237px;height:356px;border:1px solid #ddd;background:linear-gradient(#f1f1f1,#f7f7f7)}
.contact h2{position:absolute;left:15px;top:11px;font-family:"Cabin",sans-serif;font-weight:400;font-size:20px;color:var(--teal)}
.contact .note{position:absolute;left:17px;top:40px;font-size:10px;letter-spacing:.3px;color:#333}
.contact .field{position:absolute;left:15px;width:190px;height:25px;background:#fff;border:1px solid #ccc;font-size:9.5px;letter-spacing:.4px;color:#777;padding:6px 7px}
.contact .submit{position:absolute;left:125px;top:318px;width:80px;height:25px;background:var(--orange);border-radius:2px;color:#fff;font-family:"Arimo",sans-serif;font-weight:700;font-size:12px;display:flex;align-items:center;justify-content:center}

.footer{top:1029px;left:0;width:927px;height:171px;background:var(--footer);font-family:"Arimo",sans-serif;color:var(--footer-text)}
.footer h4{position:absolute;top:20px;font-family:"Cabin",sans-serif;font-weight:400;font-size:18px;color:#ddd;padding-bottom:10px;border-bottom:1px solid #4a4a4a}
.footer .links{position:absolute;left:90px;top:70px;list-style:none;font-size:9.5px;line-height:20px}
.footer .tweet{position:absolute;left:222px;top:80px;width:255px;font-size:9px;line-height:12px}
.footer .tweet .avatar{position:absolute;left:0;top:0;width:24px;height:22px;background:#8a6a4a}
.footer .tweet .who{margin-left:28px;font-weight:700}
.footer .tweet .handle{margin-left:28px;color:#aaa}
.footer .tweet .date{position:absolute;right:20px;top:0;font-size:8px;color:#bbb}
.footer .tweet p{margin-top:6px}
.footer .text{position:absolute;top:76px;font-size:9.5px;line-height:15.5px}
.footer .subscribe{position:absolute;left:503px;top:1160px;margin-top:-1029px;width:177px;height:25px;background:#e9e9e9;font-size:9px;color:#999;display:flex;align-items:center;gap:8px;padding-left:8px}
.footer .mark{position:absolute;left:716px;top:122px;font-family:"Cabin",sans-serif;font-weight:500;font-size:24px;color:#777;letter-spacing:1px}
.footer .mark small{display:block;font-size:9px;font-weight:400;letter-spacing:.5px;margin-top:-2px}
</style>
</head>
<body>

<div class="abs topbar">
  <div class="abs item" style="left:565px">
    <svg width="18" height="12" viewBox="0 0 18 12"><rect x="0.5" y="0.5" width="17" height="11" fill="#3aa7c4"/><path d="M1 1l8 6 8-6" stroke="#fff" fill="none" stroke-width="1.2"/></svg>
    hello@klevmatrexa.eu
  </div>
  <div class="abs item phone" style="left:712px">
    <svg width="15" height="15" viewBox="0 0 24 24"><path fill="#3aa7c4" d="M6.6 10.8a15.1 15.1 0 0 0 6.6 6.6l2.2-2.2a1 1 0 0 1 1-.25 11.4 11.4 0 0 0 3.6.57 1 1 0 0 1 1 1V20a1 1 0 0 1-1 1A17 17 0 0 1 3 4a1 1 0 0 1 1-1h3.5a1 1 0 0 1 1 1c0 1.25.2 2.45.57 3.57a1 1 0 0 1-.25 1z"/></svg>
    +44-7700-900318
  </div>
</div>

<div class="abs logo">
  <div class="name">KLEV <i></i></div>
  <div class="tag">quiet on the earth</div>
</div>

<nav class="abs nav">
  <span class="marker"></span>
  <a class="active" href="#" style="left:436px">HOME</a>
  <a href="#" style="left:510px">PAGES</a>
  <a href="#" style="left:590px">FEATURES</a>
  <a href="#" style="left:682px">BLOG</a>
  <a href="#" style="left:755px">WORK</a>
</nav>

<section class="abs hero" role="img" aria-label="Soft-focus kitchen backdrop with stacked translucent food storage containers with blue, yellow and orange lids">
  <div class="product"></div>
  <h1>Bio-Neutral Plastic</h1>
  <div class="rule" style="top:120px"></div>
  <div class="sub">KLEV Matrexa Technologies AG</div>
  <div class="rule" style="top:163px"></div>
  <div class="btn">More Information</div>
  <div class="arrow" style="left:17px"><svg width="10" height="12" viewBox="0 0 10 12"><path d="M7 1L2 6l5 5" stroke="#fff" stroke-width="2.2" fill="none"/></svg></div>
  <div class="arrow" style="left:877px"><svg width="10" height="12" viewBox="0 0 10 12"><path d="M3 1l5 5-5 5" stroke="#fff" stroke-width="2.2" fill="none"/></svg></div>
</section>

<section class="audience">
  <div class="abs" style="left:78px;top:450px">
    <h2><i style="background:#c9d23a"></i>Plastic compounders</h2>
    <p>when an unknown printer took a galley of type and scrambled it to make a type speci-men book. It has survived not only five cen-turies, but also the leap into electronic.</p>
  </div>
  <div class="abs" style="left:360px;top:448px">
    <h2><i style="background:#555"></i>Plastic converters</h2>
    <p>when an unknown printer took a galley of type and scrambled it to make a type speci-men book. It has survived not only five cen-turies, but also the leap into electronic.</p>
  </div>
  <div class="abs" style="left:628px;top:446px">
    <h2><i style="background:#e86a4a"></i>Brand owners</h2>
    <p>when an unknown printer took a galley of type and scrambled it to make a type speci-men book. It has survived not only five cen-turies, but also the leap into electronic.</p>
  </div>
</section>

<div class="abs divider"></div>

<section class="work">
  <article class="abs" style="left:78px;top:626px">
    <div class="thumb" role="img" aria-label="Row of green plastic bottles" style="background:linear-gradient(180deg,#e6f2ea,#3fa866 55%,#1f7d45)"></div>
    <h3>Save the World</h3>
    <div class="meta">0 MAY 2013 - DESIGN, PRINT</div>
  </article>
  <article class="abs" style="left:350px;top:627px">
    <div class="thumb" role="img" aria-label="Heap of clear plastic bottles with coloured caps" style="background:linear-gradient(135deg,#dfe6ee,#b8c8d8 50%,#9fb6cc)"></div>
    <h3>Mall Admirer</h3>
    <div class="meta">0 MAY 2013 - DESIGN, PRINT</div>
  </article>
  <article class="abs" style="left:78px;top:816px">
    <div class="thumb" role="img" aria-label="Assorted colourful plastic containers" style="background:linear-gradient(135deg,#e98a4a,#d44a4a 40%,#4a5aa0 70%,#e6e0d8)"></div>
    <h3>Spoilt for choice</h3>
    <div class="meta">0 MAY 2013 - DESIGN, PRINT</div>
  </article>
  <article class="abs" style="left:350px;top:818px">
    <div class="thumb" role="img" aria-label="Hand holding red and blue plastic pellets" style="background:linear-gradient(90deg,#e8442a,#d9673a 45%,#6aa6d8 60%,#3c86c8)"></div>
    <h3>Busy girl</h3>
    <div class="meta">0 MAY 2013 - DESIGN, PRINT</div>
  </article>
</section>

<form class="abs contact">
  <h2>Contact Information</h2>
  <div class="note">simply dummy text of and typesetting</div>
  <div class="field" style="top:63px">Name</div>
  <div class="field" style="top:100px">Last Name</div>
  <div class="field" style="top:136px">Email Address</div>
  <div class="field" style="top:173px">Phone</div>
  <div class="field" style="top:209px">Country</div>
  <div class="field" style="top:246px;height:55px">Message</div>
  <div class="submit">Submit</div>
</form>

<footer class="abs footer">
  <h4 style="left:90px;width:104px">Navigation</h4>
  <ul class="links">
    <li>Manifeste</li><li>Opportunités</li><li>Klev Friendly</li><li>Postuler</li>
  </ul>

  <h4 style="left:222px;width:253px">Latest tweets</h4>
  <div class="tweet">
    <div class="avatar"></div>
    <div class="date">11 Jul</div>
    <div class="who">Northlight</div>
    <div class="handle">@TheNorthlight</div>
    <p>We are in the final stages of building our latest product - Solenne for PressLeaf. It's going to use the amazing ShopLeaf plugin.</p>
  </div>

  <h4 style="left:503px;width:177px">Newsletter</h4>
  <div class="text" style="left:503px;width:180px">Vestibulum at lacus id turpis malesuada varius. Donec ultricies mauris vel nisi porta dictum.</div>
  <div class="subscribe">
    <svg width="11" height="8" viewBox="0 0 11 8"><rect x=".5" y=".5" width="10" height="7" fill="none" stroke="#666"/><path d="M.5.5l5 4 5-4" stroke="#666" fill="none"/></svg>
    e-mail address
  </div>

  <h4 style="left:707px;width:140px">About us</h4>
  <div class="text" style="left:707px;width:145px">Solenne is a modern responsive HTML5 theme</div>
  <div class="mark">KLEV<small>quiet on the earth</small></div>
</footer>

</body>
</html>
```